Brochure style flyer design required for Baby Boutique

We would like to create 2 flyers for our baby boutique business, the first is a basic A5 single sided one to hand out at fairs, leaflet drop at peoples home etc. It needs to show a little of what we do, our logo and contact details.
The second needs to be a booklet style to show more of what we do, almost liek a mini catalogue. It will be A5 and a folded booklet with 8 pages, including the front cover.
Our logo and some product images are attached. Contact details are as follows'
Email - sales@maplewrenbabyboutique.example
website - www.maplewrenbabyboutique.example
Facebook - Maple Wren Baby Boutique
Instagram - maplewrenbabyboutique
Twitter - @maplewrenbaby
Telephone number - +44 (0)7000 514276

Please check out our website to get some text for the flyers, we may change/update the text for the fylers once the winning design has been chosen.

We are a middle to high end baby brand so the designs need to demonstrate this

Thank you

Target Market(s)

mums to be, new mums

Industry/Entity Type

Business

Contact Information for Business Card

Website address, telephone number, email address to definitely be on there, facebook, twitter and instagram preferrably too

```html
<!DOCTYPE html>
<html lang="en">
<head>
<meta charset="utf-8">
<title>Maple Wren Baby Boutique – Flyer</title>
<link rel="stylesheet" href="https://fonts.googleapis.com/css2?family=Open+Sans:wght@400;600;700;800&display=swap">
<style>
  :root {
    --pink: #f3a6c2;
    --pink-deep: #e889ad;
    --aqua: #9fe1df;
    --aqua-deep: #6fcfcc;
    --grey: #8b8b8d;
    --grey-dark: #3c3c3e;
    --white: #ffffff;
    --photo-baby: #d9cfc8;
    --photo-pram: #c9a9a4;
    --photo-cot: #a8796a;
  }
  * { box-sizing: border-box; margin: 0; padding: 0; }
  html, body { width: 900px; height: 1200px; overflow: hidden; }
  body {
    position: relative;
    background: var(--grey);
    font-family: "Open Sans", Arial, sans-serif;
    color: var(--white);
  }
  .hero { position: absolute; left: 0; top: 0; width: 900px; height: 640px; }
  .brand {
    position: absolute; right: 60px; top: 70px; width: 260px;
    text-align: center; color: var(--grey);
    font-weight: 600; font-size: 30px; line-height: 1.1; letter-spacing: 1px;
  }
  .brand small {
    display: inline-block; font-size: 13px; letter-spacing: 3px; margin-top: 8px;
    padding: 3px 14px; border-radius: 12px; background: #f6ecd9; color: var(--grey);
  }
  .tagline-ribbon { position: absolute; left: 40px; top: 660px; width: 820px; height: 80px; }
  .tagline {
    position: absolute; left: 0; top: 678px; width: 900px; text-align: center;
    font-weight: 800; font-size: 33px; color: var(--grey-dark); letter-spacing: 0.5px;
    white-space: nowrap;
  }
  .about { position: absolute; left: 70px; top: 780px; width: 760px; }
  .about h2 {
    color: var(--pink); font-weight: 800; font-size: 24px; letter-spacing: 2px; margin-bottom: 12px;
  }
  .about p { font-size: 14px; line-height: 1.45; margin-bottom: 12px; }
  .contact {
    position: absolute; left: 250px; top: 990px; width: 400px; height: 96px;
    background: var(--white); border-radius: 20px; border-top: 8px solid var(--pink);
    padding: 12px 24px; color: var(--aqua-deep); font-weight: 600;
  }
  .contact-row { display: flex; align-items: center; gap: 12px; height: 36px; white-space: nowrap; }
  .contact-row svg { flex-shrink: 0; }
  .contact-row.phone { font-size: 22px; color: var(--grey-dark); }
  .contact-row.email { font-size: 15px; }
  .footer {
    position: absolute; left: 0; bottom: 0; width: 900px; height: 90px;
    background: var(--aqua); border-top: 8px solid var(--pink);
    display: flex; align-items: center; justify-content: space-between;
    padding: 0 36px; color: var(--grey-dark);
  }
  .socials { display: flex; align-items: center; gap: 20px; }
  .social {
    display: flex; align-items: center; gap: 7px;
    font-size: 11px; font-weight: 600; white-space: nowrap;
  }
  .social-dot {
    flex-shrink: 0; width: 16px; height: 16px; border-radius: 50%; background: var(--white);
  }
  .website { font-size: 15px; font-weight: 700; white-space: nowrap; }
</style>
</head>
<body>
  <svg class="hero" viewBox="0 0 900 640">
    <rect width="900" height="640" fill="var(--white)"/>
    <path d="M0 560 Q420 700 900 520 L900 640 L0 640Z" fill="var(--grey)"/>
    <path d="M0 520 Q420 660 900 480 L900 520 Q420 700 0 560Z" fill="var(--aqua)"/>
    <path d="M0 500 Q420 640 900 460 L900 480 Q420 660 0 520Z" fill="var(--pink)"/>
    <circle cx="230" cy="220" r="310" fill="var(--aqua)"/>
    <circle cx="230" cy="220" r="296" fill="var(--pink)"/>
    <circle cx="230" cy="220" r="282" fill="var(--photo-baby)" role="img" aria-label="Photo of a baby in a soft white winter hat"/>
    <circle cx="565" cy="380" r="132" fill="var(--pink)"/>
    <circle cx="565" cy="380" r="120" fill="var(--photo-pram)" stroke="var(--white)" stroke-width="6" role="img" aria-label="Photo of a vintage white lace pram"/>
    <circle cx="780" cy="420" r="132" fill="var(--aqua)"/>
    <circle cx="780" cy="420" r="120" fill="var(--photo-cot)" stroke="var(--white)" stroke-width="6" role="img" aria-label="Photo of a cot with patterned nursery bedding"/>
  </svg>

  <div class="brand">maple wren<br><small>BABY BOUTIQUE</small></div>

  <svg class="tagline-ribbon" viewBox="0 0 820 80" aria-hidden="true">
    <path d="M0 10 L820 10 L795 40 L820 70 L0 70 L25 40Z" fill="var(--pink)"/>
  </svg>
  <h1 class="tagline">YOUR ONE STOP BESPOKE BABY SHOP</h1>

  <section class="about">
    <h2>ABOUT US</h2>
    <p>Here at Maple Wren Baby Boutique we are proud to offer a unique, personalised nursery design service. With a vast selection of fabric choices we can tailor your babys' bedding, curtains and even wardrobe to suit your individual tastes.</p>
    <p>As part of our commitment to bringing you bespoke, custom designs we offer global fabric sourcing, free of charge for each and every client. Alternatively if you know the exact fabric and design you would like we can work with you to deliver your vision.</p>
  </section>

  <div class="contact">
    <div class="contact-row phone">
      <svg width="22" height="22" viewBox="0 0 24 24" aria-hidden="true"><path d="M6.6 10.8a15 15 0 0 0 6.6 6.6l2.2-2.2a1 1 0 0 1 1-.25 11.4 11.4 0 0 0 3.6.57 1 1 0 0 1 1 1V20a1 1 0 0 1-1 1A17 17 0 0 1 3 4a1 1 0 0 1 1-1h3.5a1 1 0 0 1 1 1c0 1.25.2 2.45.57 3.57a1 1 0 0 1-.25 1z" fill="var(--pink-deep)"/></svg>
      +44 (0)7000 514276
    </div>
    <div class="contact-row email">
      <svg width="22" height="22" viewBox="0 0 24 24" aria-hidden="true"><rect x="2" y="5" width="20" height="14" rx="2" fill="var(--pink-deep)"/><path d="M3 6l9 7 9-7" stroke="var(--white)" stroke-width="1.6" fill="none"/></svg>
      sales@maplewrenbabyboutique.example
    </div>
  </div>

  <footer class="footer">
    <div class="socials">
      <span class="social"><span class="social-dot"></span>Maple Wren Baby Boutique</span>
      <span class="social"><span class="social-dot"></span>@maplewrenbaby</span>
      <span class="social"><span class="social-dot"></span>maplewrenbabyboutique</span>
    </div>
    <span class="website">www.maplewrenbabyboutique.example</span>
  </footer>
</body>
</html>
```